Wine label design

Need a logo/design for new wine label.
All we have is a label name which is "Varnelposi"
The vineyard is located on rocky hills but we dont really have any design concept in mind. We would like a fun but modern label.

Target Market(s)

Wine consumers. Not too serious. Premium quality product but should be fun and easy to recognise.

Industry/Entity Type

Vineyard

Colors

Designer to choose colors to be used in the design.

Requirements
Must have
• Simple, standout logo/label name
• Contemporary, modern, funky label
• Flexible on colour scheme. Would like it to stand-out and be recognisable but still needs an element of class that reflects premium quality wine.
Nice to have
• Potentially have a link to rolling hills of exposed rock that we produce from.
Should not have
• Old, traditional style label

```html
<!DOCTYPE html>
<html lang="en">
<head>
<meta charset="UTF-8">
<title>Varnelposi — Red Wine Label</title>
<link href="https://fonts.googleapis.com/css2?family=Poiret+One&family=Quicksand:wght@400;500&display=swap" rel="stylesheet">
<style>
  :root {
    --backdrop: #1c080d;
    --label-deep: #1f070c;
    --label-mid: #3b0f19;
    --ink-light: #eef6f8;
    --ink-glow: rgba(150, 220, 235, 0.55);
    --wine-red: #7a1420;
    --copper: #a8593c;
    --navy: #16253a;
    --mauve: #9a5f78;
  }
  html, body {
    margin: 0;
    padding: 0;
    width: 1200px;
    height: 1000px;
    overflow: hidden;
    background: var(--backdrop);
  }
  .label {
    position: absolute;
    left: 262px;
    top: 15px;
    width: 676px;
    height: 970px;
    overflow: hidden;
    background: radial-gradient(ellipse at 50% 30%, var(--label-mid) 0%, var(--label-deep) 75%);
  }
  .origin {
    position: absolute;
    top: 80px;
    width: 100%;
    text-align: center;
    font-family: "Quicksand", sans-serif;
    font-weight: 500;
    font-size: 20px;
    color: var(--ink-light);
  }
  .wine-name {
    position: absolute;
    top: 108px;
    width: 100%;
    margin: 0;
    text-align: center;
    font-family: "Poiret One", sans-serif;
    font-weight: 400;
    font-size: 76px;
    letter-spacing: 1px;
    color: transparent;
    -webkit-text-stroke: 1.6px var(--ink-light);
    text-shadow: 0 0 6px var(--ink-glow);
  }
  .pattern-area {
    position: absolute;
    left: 0;
    top: 260px;
    width: 676px;
    height: 710px;
  }
  .bottom-text {
    position: absolute;
    font-family: "Poiret One", sans-serif;
    color: transparent;
    -webkit-text-stroke: 1.2px var(--ink-light);
    text-shadow: 0 0 6px rgba(0, 0, 0, 0.8);
  }
  .wine-type {
    left: 32px;
    top: 886px;
    font-size: 32px;
  }
  .alcohol {
    right: 58px;
    top: 886px;
    font-size: 32px;
  }
  .quality-mark {
    position: absolute;
    left: 0;
    width: 100%;
    top: 852px;
    text-align: center;
    font-family: "Quicksand", sans-serif;
    color: var(--ink-light);
    text-shadow: 0 0 8px rgba(0, 0, 0, 0.9);
    line-height: 1;
  }
  .quality-mark .premium {
    display: block;
    font-size: 44px;
    font-weight: 500;
  }
  .quality-mark .quality {
    display: block;
    font-size: 30px;
    font-weight: 400;
    margin-top: -4px;
  }
</style>
</head>
<body>
  <main class="label">
    <div class="origin">Made in Rocky Hills</div>
    <h1 class="wine-name">VARNELPOSI</h1>

    <svg class="pattern-area" viewBox="0 0 676 710" role="img" aria-label="Interlaced ribbon knot pattern in wine red, copper, navy and mauve rising like rocky hills">
      <defs>
        <linearGradient id="ribbonTones" x1="0" y1="0" x2="1" y2="1">
          <stop offset="0" stop-color="var(--copper)"/>
          <stop offset="0.35" stop-color="var(--wine-red)"/>
          <stop offset="0.65" stop-color="var(--navy)"/>
          <stop offset="1" stop-color="var(--mauve)"/>
        </linearGradient>
      </defs>
      <path d="M0 290 L150 210 L200 160 L300 250 L350 90 L470 170 L560 10 L676 140 L676 710 L0 710 Z"
            fill="url(#ribbonTones)" opacity="0.75"/>
    </svg>

    <div class="bottom-text wine-type">RED WINE</div>
    <div class="quality-mark">
      <span class="premium">premium</span>
      <span class="quality">quality</span>
    </div>
    <div class="bottom-text alcohol">N%ALC</div>
  </main>
</body>
</html>
```